VelaMend Wellness Business Cards

I am looking to have luxury business cards made for my IV Therapy and Wellness business.

Target Market(s)

Health and Wellness professionals

Industry/Entity Type

MedSpa

Contact Information for Business Card

Tobin Hargreave, MSN, RN, CCRN Tobin@velamendwellness.com (916) 582-1937 QR code to website www.velamendwellness.com

```html
<!DOCTYPE html>
<html lang="en">
<head>
<meta charset="utf-8">
<title>VelaMend Wellness Business Cards</title>
<link rel="stylesheet" href="https://fonts.googleapis.com/css2?family=Montserrat:wght@400;500;600;700;800&display=swap">
<style>
  :root {
    --backdrop: #2a2a2a;
    --navy: #24235f;
    --navy-deep: #1f1f55;
    --sky: #2fa3e0;
    --sky-soft: #3a8fd0;
    --ink: #1b1b1b;
    --rule: #b9b9b9;
    --paper: #ffffff;
  }
  * { box-sizing: border-box; margin: 0; padding: 0; }
  html, body { width: 1200px; height: 800px; overflow: hidden; }
  body {
    background: var(--backdrop);
    font-family: "Montserrat", Arial, sans-serif;
    position: relative;
  }
  .card {
    position: absolute;
    width: 520px;
    height: 297px;
    border-radius: 22px;
    overflow: hidden;
    box-shadow: 0 14px 30px rgba(0,0,0,0.45);
  }
  .card--front { left: 50px; top: 90px; background: var(--navy); }
  .card--back { left: 630px; top: 413px; background: var(--paper); }

  .drop-field {
    position: absolute; inset: 0;
    background: linear-gradient(215deg, var(--sky-soft) 0%, #2c5a9a 28%, var(--navy) 58%, var(--navy-deep) 100%);
  }
  .front-mark {
    position: absolute; inset: 0;
    display: flex; align-items: center; justify-content: center; gap: 10px;
    color: var(--paper);
    font-weight: 700;
    font-size: 34px;
    letter-spacing: 0.5px;
    white-space: nowrap;
  }
  .mark-dot {
    flex: 0 0 auto;
    width: 14px; height: 14px; border-radius: 50%;
    background: var(--sky);
  }

  .back-mark {
    position: absolute; left: 26px; top: 196px; width: 222px;
    display: flex; align-items: center; gap: 7px;
    color: var(--navy);
    font-weight: 700;
    font-size: 18px;
    white-space: nowrap;
  }
  .back-mark .mark-dot { width: 9px; height: 9px; }

  .divider {
    position: absolute; left: 262px; top: 44px;
    width: 1px; height: 210px; background: var(--rule);
  }
  .details { position: absolute; left: 288px; top: 56px; right: 18px; }
  .person-name {
    font-weight: 800; font-size: 18px; color: var(--navy);
    letter-spacing: 0.3px; white-space: nowrap;
  }
  .person-name .surname { color: var(--sky); }
  .name-rule { height: 1px; background: var(--rule); margin: 6px 0 4px 70px; }
  .person-title { font-size: 11px; font-weight: 500; color: var(--ink); letter-spacing: 0.5px; margin-bottom: 12px; }
  .contact-list { list-style: none; }
  .contact-list li {
    display: flex; align-items: flex-start; gap: 9px;
    font-size: 11.5px; color: var(--ink); line-height: 1.25; margin-bottom: 6px;
    white-space: nowrap;
  }
  .contact-icon { flex: 0 0 13px; width: 13px; height: 13px; margin-top: 1px; }
</style>
</head>
<body>
  <section class="card card--front" aria-label="Business card front">
    <div class="drop-field" role="img" aria-label="Pattern of water droplets fading from navy to sky blue"></div>
    <div class="front-mark"><span class="mark-dot"></span><span>VelaMend Wellness</span></div>
  </section>

  <section class="card card--back" aria-label="Business card back">
    <div class="back-mark"><span class="mark-dot"></span><span>VelaMend Wellness</span></div>
    <div class="divider"></div>
    <div class="details">
      <p class="person-name">TOBIN <span class="surname">HARGREAVE</span></p>
      <div class="name-rule"></div>
      <p class="person-title">MSN, RN, CCRN</p>
      <ul class="contact-list">
        <li>
          <svg class="contact-icon" viewBox="0 0 13 13" aria-hidden="true"><rect width="13" height="13" rx="2" fill="#2fa3e0"/><rect x="4" y="2.5" width="5" height="8" rx="1" fill="none" stroke="#fff" stroke-width="1.2"/></svg>
          <span>(916) 582-1937</span>
        </li>
        <li>
          <svg class="contact-icon" viewBox="0 0 13 13" aria-hidden="true"><rect width="13" height="13" rx="2" fill="#2fa3e0"/><path d="M3 6.5 L10 3 L7.5 10 L6.3 7.3 Z" fill="#fff"/></svg>
          <span>Tobin@velamendwellness.com</span>
        </li>
        <li>
          <svg class="contact-icon" viewBox="0 0 13 13" aria-hidden="true"><rect width="13" height="13" rx="2" fill="#2fa3e0"/><circle cx="6.5" cy="6.5" r="3.6" fill="none" stroke="#fff" stroke-width="1"/><path d="M2.9 6.5 H10.1 M6.5 2.9 V10.1" stroke="#fff" stroke-width="0.8"/></svg>
          <span>www.velamendwellness.com</span>
        </li>
        <li>
          <svg class="contact-icon" viewBox="0 0 13 13" aria-hidden="true"><rect width="13" height="13" rx="2" fill="#2fa3e0"/><path d="M6.5 2.5 a3 3 0 0 1 3 3 c0 2-3 5-3 5 s-3-3-3-5 a3 3 0 0 1 3-3z" fill="#fff"/><circle cx="6.5" cy="5.5" r="1.1" fill="#2fa3e0"/></svg>
          <span>4471 Harbor Reed Pkwy,<br>212-B, FL 32561</span>
        </li>
      </ul>
    </div>
  </section>
</body>
</html>
```